CrestwayGuides Summer Brunch

This flyer is designed to market the upcoming conference in July

Target Market(s)

African American Christian Men and Women

Font styles to use
Decorative

Requirements
Must have
• This flyer is to represent both men and women as follows:
• Although offered on the same day and same location - Men and Women must appear two meetings in one location
• 1. SOB - Sons of Bright
• 2. GAVU - Gentle and Very Uplifted - Women
• Theme: "2020 - Rising With Grace" (Ephesians 6:10-15)
• Date: June 27, 2020
Nice to have
• *Distinct between the two meetings in one
• * Unified brand coupled with Men and Women targets
• * Vibrant, energized, active flyer to communicate promise and hope
Should not have
• Profanity, clip art, etc.

```html
<!DOCTYPE html>
<html lang="en">
<head>
<meta charset="utf-8">
<title>CrestwayGuides – Rising With Grace</title>
<link rel="stylesheet" href="https://fonts.googleapis.com/css2?family=Cinzel:wght@400;600&family=Cormorant+Garamond:wght@500&family=Montserrat:wght@500&family=Oswald:wght@500;600&family=Sorts+Mill+Goudy&display=swap">
<style>
  :root {
    --black: #000000;
    --night: #0d0d0d;
    --gold: #7a6940;
    --gold-deep: #6c5c36;
    --gold-text: #8c7746;
    --white: #f1f0ec;
    --silver: #bdbdbd;
  }
  * { box-sizing: border-box; margin: 0; padding: 0; }
  html, body { width: 902px; height: 1200px; overflow: hidden; background: var(--black); }
  .flyer { position: relative; width: 902px; height: 1200px; overflow: hidden; color: var(--white); }

  .masthead { position: absolute; inset: 0 0 auto 0; height: 238px; background: var(--black); }
  .brand-name {
    position: absolute; top: 128px; left: 0; width: 100%; text-align: center;
    font-family: "Sorts Mill Goudy", serif; font-size: 60px; line-height: 1; color: var(--white);
  }
  .tagline {
    position: absolute; top: 209px; left: 0; width: 100%; text-align: center;
    font-family: "Montserrat", sans-serif; font-size: 12.5px; letter-spacing: 1.6px;
    text-transform: uppercase; color: var(--gold-text);
  }

  .panel { position: absolute; top: 238px; bottom: 0; }
  .panel-women {
    left: 0; width: 451px;
    background: radial-gradient(ellipse 70% 50% at 40% 35%, #86744a 0%, var(--gold) 55%, var(--gold-deep) 100%);
  }
  .panel-men {
    left: 451px; right: 0;
    background: radial-gradient(ellipse 60% 45% at 45% 30%, #1d1d1d 0%, var(--night) 60%, #050505 100%);
  }

  .meeting { position: absolute; top: 268px; text-align: center; }
  .meeting-women { left: 20px; width: 410px; }
  .meeting-men { left: 508px; width: 350px; }
  .meeting-title {
    font-family: "Cinzel", serif; font-weight: 400; font-size: 56px; line-height: 1; letter-spacing: 22px;
    padding-left: 22px; color: var(--white);
  }
  .meeting-sub {
    margin-top: 18px; padding-bottom: 8px;
    font-family: "Cinzel", serif; font-size: 11px; letter-spacing: 5.5px; color: var(--white);
    border-bottom: 1px solid rgba(190,190,190,0.45);
  }

  .year-box {
    position: absolute; left: 277px; top: 394px; width: 350px; height: 126px;
    background: var(--white); border-radius: 8px;
  }
  .year {
    display: block; width: 100%; text-align: center;
    font-family: "Cinzel", serif; font-weight: 600; font-size: 96px; line-height: 126px; letter-spacing: 8px; padding-left: 8px;
    background: linear-gradient(90deg, var(--gold) 0 173px, var(--black) 173px);
    -webkit-background-clip: text; background-clip: text; color: transparent;
  }

  .theme-word {
    position: absolute; top: 532px; width: 902px; text-align: center;
    font-family: "Oswald", sans-serif; font-weight: 600; font-size: 196px; line-height: 1;
    letter-spacing: 6px; text-transform: uppercase;
  }
  .theme-word-shadow {
    left: 6px; top: 538px;
    background: linear-gradient(90deg, var(--black) 0 445px, var(--gold-text) 445px);
    -webkit-background-clip: text; background-clip: text; color: transparent;
  }
  .theme-word-face { left: 0; color: var(--white); }

  .rule {
    position: absolute; left: 57px; width: 775px; height: 2px;
    background: linear-gradient(90deg, transparent, var(--silver) 30%, #e4e4e4 50%, var(--silver) 70%, transparent);
  }
  .rule-top { top: 733px; }
  .rule-bottom { top: 815px; }
  .theme-line {
    position: absolute; top: 744px; left: 0; width: 902px; text-align: center;
    font-family: "Cinzel", serif; font-size: 64px; line-height: 66px; letter-spacing: 28px; padding-left: 28px;
    text-transform: uppercase; color: var(--white);
  }
  .scripture {
    position: absolute; top: 840px; left: 0; width: 902px; text-align: center;
    font-family: "Cinzel", serif; font-weight: 400; font-size: 40px; line-height: 1; letter-spacing: 1px;
    color: var(--white);
  }

  .date-box { position: absolute; left: 160px; top: 917px; width: 583px; height: 141px; border-radius: 8px; overflow: hidden; display: flex; }
  .date-when {
    width: 291px; background: var(--black); display: flex; align-items: center; justify-content: center; gap: 8px;
    font-family: "Cinzel", serif; font-size: 15px; color: var(--white);
  }
  .date-when .day-num { font-family: "Oswald", sans-serif; font-weight: 600; font-size: 40px; line-height: 1; }
  .date-save { flex: 1; background: var(--gold); text-align: center; padding-top: 8px; }
  .save-small { display: block; font-family: "Cinzel", serif; font-size: 36px; line-height: 44px; letter-spacing: 2px; }
  .save-big { display: block; font-family: "Cinzel", serif; font-size: 84px; line-height: 84px; }

  .info {
    position: absolute; top: 1087px; left: 0; width: 902px; text-align: center;
    font-family: "Cinzel", serif; font-size: 24px; letter-spacing: 1px; color: var(--white);
  }
  .web { position: absolute; top: 1126px; left: 56px; display: flex; align-items: center; gap: 20px; }
  .web-icon { width: 34px; height: 34px; }
  .web-url {
    font-family: "Cinzel", serif; font-size: 40px; line-height: 50px; letter-spacing: 3px; color: var(--white);
    white-space: nowrap;
  }
</style>
</head>
<body>
<main class="flyer">
  <header class="masthead">
    <div class="brand-name">CrestwayGuides</div>
    <div class="tagline">Guiding Hearts, Building Neighborhoods</div>
  </header>

  <div class="panel panel-women" role="img" aria-label="Soft gold-toned photograph of women in worship"></div>
  <div class="panel panel-men" role="img" aria-label="Dark photograph of men in prayer"></div>

  <section class="meeting meeting-women">
    <h2 class="meeting-title">GAVU</h2>
    <p class="meeting-sub">GENTLE AND VERY UPLIFTED</p>
  </section>
  <section class="meeting meeting-men">
    <h2 class="meeting-title">SOB</h2>
    <p class="meeting-sub">SONS OF BRIGHT</p>
  </section>

  <div class="year-box"><span class="year">2020</span></div>

  <div class="theme-word theme-word-shadow" aria-hidden="true">Rising</div>
  <h1 class="theme-word theme-word-face">Rising</h1>

  <div class="rule rule-top"></div>
  <div class="theme-line">With Grace</div>
  <div class="rule rule-bottom"></div>

  <p class="scripture">[EPHESIANS 6:10-15]</p>

  <div class="date-box">
    <div class="date-when"><span>JUNE</span><span class="day-num">27,2020</span><span>SATURDAY</span></div>
    <div class="date-save"><span class="save-small">SAVE THE</span><span class="save-big">DATE</span></div>
  </div>

  <p class="info">VISIT US FOR MORE INFORMATION</p>
  <div class="web">
    <svg class="web-icon" viewBox="0 0 36 36" fill="none" stroke="#e6e6e6" stroke-width="2" aria-hidden="true">
      <circle cx="18" cy="18" r="15"/>
      <ellipse cx="18" cy="18" rx="7" ry="15"/>
      <line x1="3" y1="18" x2="33" y2="18"/>
      <line x1="6" y1="10" x2="30" y2="10"/>
      <line x1="6" y1="26" x2="30" y2="26"/>
    </svg>
    <span class="web-url">WWW.CRESTWAYGUIDES.COM</span>
  </div>
</main>
</body>
</html>
```